Something different!?!?!?.....Real Estate Business Card

**01/02/2016 Update** I have added a QR code. I am liking Black cards with the Corvath Homes on the back so I do not need "Corvath homes" on the front. Please adjust with QR code somewhere without over crowding the card. Thank you!

**12/27/2015 Update** All the submissions are amazing!!! Thank you so much to every single person who has taken the time out of your day. I'm loving the black with the red but still not stuck on anything. The number one thing I would like is for my hair/ picture and everything to flow into the background or look like I'm popping out of the card 3D without a hard choppy line. I did comment on one of the submissions that the picture flowed great. I am looking for something unique as well. I don't know what but I need my card to stand out from every other Corvath Homes agent as well as other companies in the area. They need to remember me by looking at my card. I am looking for a flyer as well that I can send out to introduce myself to the neighborhood. Maybe a happy holidays? Like a postcard looking for buyers and sellers or anyone with questions about the market. That needs to stand out as well and I would like it the same theme as the business card. Again thank you everyone who is taking the time to help me as I am illiterate when it comes to graphic design!!

I need a Business Card and a post card mailer that I can send out to people in the area. I would like to keep the same theme through out but not a must. I am an agent for Corvath Homes so their logo needs to be somewhere I have attached two. I think as long as its red around white Corvath Homes letters I'm good. I have attached a picture of me in the car if someone could take out the background and make it look professional that would be great otherwise I have also attached someone else and myself messed with (I think it looks tacky). I like when the person looks like they're floating in the background.

If like your work I will be needing someone for marketing campaign designs, etc.
Updates

Target Market(s)

MN and WI Real Estate Buyers and Sellers

Industry/Entity Type

Real Estate

Contact Information for Business Card

Tessa Brandow
WI & MN Realtor
18392 County Lane 48/61 South
Larkmoor, ST 54899
TessaBrandow@CorvathHomes.example
C: 702.555.0184
W:715.555.0162
F: 715.555.0127

Requirements
Must have
• Picture
• Contact Info
• white Corvath Homes letters with a red box
Nice to have
• 3D
Should not have
• Hard lines around picture

```html
<!DOCTYPE html>
<html lang="en">
<head>
<meta charset="utf-8">
<title>Tessa Brandow – Business Card</title>
<link rel="stylesheet" href="https://fonts.googleapis.com/css2?family=Montserrat:wght@700&family=Questrial&display=swap">
<style>
  :root {
    --page-bg: #d9d6d1;
    --card-black: #0c0c0c;
    --brand-red: #e24a4f;
    --ink-light: #e8e8e8;
    --ink-muted: #bdbdbd;
    --white: #ffffff;
  }
  * { margin: 0; padding: 0; box-sizing: border-box; }
  html, body {
    width: 1200px; height: 843px; overflow: hidden;
    background: var(--page-bg);
    font-family: "Questrial", "Century Gothic", sans-serif;
  }
  .canvas {
    position: relative; width: 1200px; height: 843px;
    display: flex; flex-direction: column; align-items: center; justify-content: center; gap: 26px;
  }
  .card {
    position: relative; width: 680px; height: 389px;
    background: var(--card-black);
    overflow: hidden;
    box-shadow: 0 6px 18px rgba(0,0,0,0.25);
  }

  /* back side */
  .address {
    position: absolute; left: 44px; top: 66px;
    color: var(--ink-light); font-size: 16px; line-height: 1.3;
  }
  .phones {
    position: absolute; left: 44px; top: 156px;
    color: var(--ink-light); font-size: 16px; line-height: 1.3;
  }
  .phones .label { color: var(--brand-red); }
  .divider {
    position: absolute; left: 232px; top: 160px;
    width: 1px; height: 96px; background: var(--ink-muted);
  }
  .online {
    position: absolute; left: 252px; top: 206px;
    color: var(--ink-light); font-size: 17px; line-height: 1.35;
    white-space: nowrap;
  }
  .brand-box {
    position: absolute; right: 40px; top: 72px;
    width: 230px; height: 66px;
    background: var(--brand-red);
    display: flex; align-items: center; justify-content: center;
  }
  .brand-name {
    color: var(--white); font-family: "Questrial", sans-serif;
    font-size: 27px; letter-spacing: -0.5px; white-space: nowrap;
  }

  /* front side */
  .portrait {
    position: absolute; left: 0; top: 0; width: 500px; height: 389px;
    background: radial-gradient(ellipse 45% 60% at 45% 48%, #6b5348 0%, #3d2d29 40%, #1a1414 70%, var(--card-black) 100%);
  }
  .name-band {
    position: absolute; right: 0; top: 0; width: 180px; height: 389px;
    background: var(--brand-red);
  }
  .name-block {
    position: absolute; left: 50%; top: 50%;
    transform: translate(-50%, -50%) rotate(-90deg);
    width: 350px; color: var(--white); white-space: nowrap;
  }
  .agent-name {
    font-family: "Montserrat", sans-serif; font-weight: 700;
    font-size: 44px; line-height: 1.05;
  }
  .agent-title { font-size: 36px; line-height: 1.15; }
</style>
</head>
<body>
<main class="canvas">
  <section class="card card-back">
    <p class="address">18392 County Lane<br>48/61 South<br>Larkmoor, ST 54899</p>
    <p class="phones">
      <span class="label">P :</span> 715.555.0162<br>
      <span class="label">C :</span> 702.555.0184<br>
      <span class="label">F :</span> 715.555.0127
    </p>
    <div class="divider"></div>
    <p class="online">TessaBrandow@CorvathHomes.example<br>www.tessabrandow.example</p>
    <div class="brand-box"><span class="brand-name">Corvath Homes</span></div>
  </section>

  <section class="card card-front">
    <div class="portrait" role="img" aria-label="Portrait photo of the agent with long wavy hair, fading into the black card"></div>
    <div class="name-band">
      <div class="name-block">
        <h1 class="agent-name">Tessa Brandow</h1>
        <p class="agent-title">WI &amp; MN Realtor</p>
      </div>
    </div>
  </section>
</main>
</body>
</html>
```